Stationery Design Refresh - Velmora

We are Velmora - a small training & consulting company in Australia.
We HAVE a logo, but want to tweak it (original eps files available).

We want to the following outputs:
Change our stylised 'G' and possibly the current colour scheme is blue & green - we think that does not work very well.

Once that is done, we need to translate that into a PPT master and a letterhead. (Examples of current provided.)

We need a banner (for our website) and a few treatments of the icons used in the design (explained below)

The design 'language ' we want to adopt is:
Conversation bubbles
Grafitti
Hand painting

The 'g' should be stylised as two conversation bubbles.
We want to use these bubbles - and several different ones - as a feature in PPT presentations and therefore need a PPT Master

We need the banner to reflect the above.

The banner will be used as a website header and also as a 'strip' across the bottom of the letterhead.

With the above we are trying to communicate:
Handwritten/ Involved/ Authentic
Passionate & Playful (but NOT cartoonish)
Smart/ Creative/Innovative

Target Market(s)

B2B (employees and managers)

Industry/Entity Type

Training

Requirements
Should not have
• We use blue and green at the moment. But willing to change that or use it differently. I don't want the design to be cartoons and not overly colourful - we still need a corporate feel.

```html
<!DOCTYPE html>
<html lang="en">
<head>
<meta charset="utf-8">
<title>Velmora – Learning</title>
<link href="https://fonts.googleapis.com/css2?family=Caveat+Brush&family=Open+Sans:wght@400;600;700&display=swap" rel="stylesheet">
<style>
:root{
  --stage:#2f2f2f;
  --page:#ffffff;
  --banner-dark:#2f3f52;
  --banner-mid:#4f6076;
  --banner-light:#8496ab;
  --tagline:#ffffff;
  --nav:#4a4550;
  --nav-line:#2c2930;
  --nav-text:#f1eff3;
  --body-text:#4a4a4a;
  --link:#2a4fb5;
  --brand-blue:#1f7fb0;
  --ink:#111111;
  --muted:#666666;
  --rule:#9a9a9a;
  --rss:#f08a24;
}
*{margin:0;padding:0;box-sizing:border-box}
html,body{width:1200px;height:900px;overflow:hidden;background:var(--stage)}
body{position:relative;font-family:"Open Sans",Verdana,sans-serif}
.site{position:absolute;left:54px;top:127px;width:1091px;height:580px;background:var(--page);overflow:hidden}
.banner{position:absolute;left:0;top:0;width:794px;height:211px;overflow:hidden;background:var(--banner-mid)}
.banner-texture{position:absolute;inset:0;
  background:
    radial-gradient(ellipse 60% 70% at 22% 30%,rgba(132,150,171,.75) 0%,rgba(132,150,171,0) 70%),
    radial-gradient(ellipse 50% 60% at 70% 75%,rgba(132,150,171,.55) 0%,rgba(132,150,171,0) 70%),
    radial-gradient(ellipse 55% 65% at 55% 20%,rgba(47,63,82,.7) 0%,rgba(47,63,82,0) 70%),
    linear-gradient(160deg,var(--banner-light) 0%,var(--banner-mid) 45%,var(--banner-dark) 100%)}
.tagline{position:absolute;left:82px;top:62px;font-family:"Caveat Brush","Comic Sans MS",cursive;font-size:72px;line-height:1;color:var(--tagline);letter-spacing:1px;transform:rotate(-2deg);transform-origin:left center;white-space:nowrap}
.brand{position:absolute;left:794px;top:0;width:297px;height:211px;display:flex;align-items:center;justify-content:center;gap:12px;padding-top:10px}
.brand-dot{width:22px;height:22px;border-radius:50%;background:var(--brand-blue)}
.brand-name{font-size:38px;font-weight:700;color:var(--ink);letter-spacing:-0.5px}
.nav{position:absolute;left:0;top:212px;width:1091px;height:50px;background:var(--nav);border-top:1px solid var(--nav-line);border-bottom:1px solid var(--nav-line);display:flex;align-items:center;padding-left:21px}
.nav a{color:var(--nav-text);text-decoration:none;font-size:13px;font-weight:700;letter-spacing:1.9px;margin-right:47px;white-space:nowrap}
.content{position:absolute;left:54px;top:359px;width:740px;color:var(--body-text);font-size:15.5px;line-height:27px;letter-spacing:0.5px}
.content p{margin-bottom:15px}
.content .lead{color:var(--link);font-weight:700}
.content a{color:var(--link);text-decoration:none}
.sidebar{position:absolute;left:822px;top:318px;width:216px}
.sidebar h2{font-size:14px;font-weight:400;letter-spacing:1.4px;color:var(--muted);margin-bottom:22px}
.feed{display:flex;align-items:center;gap:5px;font-size:14.5px;line-height:20px;color:var(--link);margin-bottom:24px}
.feed svg{flex:none}
.sidebar hr{border:none;border-top:2px solid var(--rule);margin:48px 0 16px}
.signup{border:1px solid #c8c8c8;padding:6px 8px 30px}
.signup span{font-size:14px;font-weight:700;color:#555;text-decoration:underline;white-space:nowrap}
.signup .field{margin:14px auto 0;width:156px;height:26px;border:1px solid #bbb}
.fade{position:absolute;left:0;top:470px;width:1091px;height:110px;background:linear-gradient(to bottom,rgba(47,47,47,0) 0%,rgba(47,47,47,0.55) 45%,var(--stage) 100%)}
</style>
</head>
<body>
<div class="site">
  <header class="banner">
    <div class="banner-texture" role="img" aria-label="Hand-painted slate-blue graffiti wall texture"></div>
    <p class="tagline">Learn to Perform</p>
  </header>
  <div class="brand"><span class="brand-dot"></span><span class="brand-name">Velmora</span></div>
  <nav class="nav">
    <a href="#">HOME</a><a href="#">BLOG</a><a href="#">SHOP</a><a href="#">JOURNAL</a><a href="#">RETAILERS</a><a href="#">FRANCHISORS</a><a href="#">SUPPLY CHAIN</a><a href="#">LEARNING</a>
  </nav>
  <main class="content">
    <p><span class="lead">Velmora Business Academy</span>&nbsp; is a full-service learning &amp; development service division.</p>
    <p>We are accredited to offer government-funded training as well as offering the full suite of commercial training services you would expect from a dynamic, innovative training company.</p>
    <p>Odette Harlan is the Principal of VBA and co-Director of VMS.</p>
    <p>For more information, please visit the <a href="#">Academy website</a>.</p>
  </main>
  <aside class="sidebar">
    <h2>SUBSCRIPTIONS</h2>
    <div class="feed"><svg width="13" height="13" viewBox="0 0 13 13"><rect width="13" height="13" rx="2" fill="var(--rss)"/><circle cx="3.5" cy="9.5" r="1.4" fill="#fff"/><path d="M2.5 6a4.5 4.5 0 0 1 4.5 4.5M2.5 3a7.5 7.5 0 0 1 7.5 7.5" stroke="#fff" stroke-width="1.4" fill="none"/></svg>blog RSS</div>
    <div class="feed"><svg width="13" height="13" viewBox="0 0 13 13"><rect width="13" height="13" rx="2" fill="var(--rss)"/><circle cx="3.5" cy="9.5" r="1.4" fill="#fff"/><path d="M2.5 6a4.5 4.5 0 0 1 4.5 4.5M2.5 3a7.5 7.5 0 0 1 7.5 7.5" stroke="#fff" stroke-width="1.4" fill="none"/></svg>blog Comments RSS</div>
    <hr>
    <div class="signup"><span>Enter email for blog posts</span><div class="field"></div></div>
  </aside>
  <div class="fade"></div>
</div>
</body>
</html>
```